Healthcare IT company looking for business card design

We develop IT systems for healthcare that significantly reduces cost and improves quality.

We want a business card design that is professional and clean, and using the colors in our logo.

Target Market(s)

Doctors and decision makers in the healthcare industry

Industry/Entity Type

Healthcare

Contact Information for Business Card

It should include
Name and title, address, telephone

Tobias Vrenholt, CEO
+46 712 418257
tobias@kelvaro.se

Font styles to use
Serif

Colors
0355a3
ed282f

Requirements
Must have
• Clean design
• Professional feel
Nice to have
• N/A
Should not have
• N/A

```html
<!DOCTYPE html>
<html lang="en">
<head>
<meta charset="utf-8">
<title>Kelvaro — Business Card</title>
<link rel="stylesheet" href="https://fonts.googleapis.com/css2?family=Source+Sans+3:wght@400;700&display=swap">
<style>
  :root {
    --brand-blue: #1560ad;
    --brand-red: #ed1f27;
    --card-white: #ffffff;
    --text-grey: #555a60;
    --backdrop: #4a3238;
  }
  * { margin: 0; padding: 0; box-sizing: border-box; }
  html, body {
    width: 1200px; height: 1200px; overflow: hidden;
    background: var(--backdrop);
    font-family: "Source Sans 3", "Myriad Pro", Arial, sans-serif;
  }
  .canvas { position: relative; width: 1200px; height: 1200px; }
  .card {
    position: absolute; left: 264px; width: 692px; height: 392px;
    overflow: hidden;
  }
  .card--front { top: 186px; background: var(--brand-blue); }
  .card--back { top: 642px; background: var(--card-white); }

  .front__wordmark {
    position: absolute; left: 0; right: 0; top: 140px;
    text-align: center; color: var(--card-white);
    font-weight: 700; font-size: 128px; line-height: 1; letter-spacing: -1px;
  }
  .front__url {
    position: absolute; left: 0; right: 0; top: 354px;
    text-align: center; color: var(--card-white);
    font-size: 18px; line-height: 1;
  }

  .back__accent {
    position: absolute; left: 0; top: 122px; width: 150px; height: 150px;
    background: var(--brand-red); border-radius: 0 10px 10px 0;
  }
  .back__divider {
    position: absolute; left: 228px; top: 48px; width: 2px; height: 298px;
    background: var(--brand-blue);
  }
  .back__wordmark {
    position: absolute; left: 258px; top: 76px;
    color: var(--brand-blue); font-weight: 700; font-size: 78px; line-height: 1; letter-spacing: -0.5px;
  }
  .back__name {
    position: absolute; left: 260px; top: 195px;
    color: var(--brand-blue); font-size: 27px; line-height: 1;
  }
  .back__title {
    position: absolute; left: 260px; top: 225px;
    color: var(--text-grey); font-size: 18px; line-height: 1;
  }
  .contact { position: absolute; left: 260px; top: 276px; list-style: none; }
  .contact__item {
    display: flex; align-items: center; gap: 10px;
    color: var(--text-grey); font-size: 19px; line-height: 23px;
  }
  .contact__icon { width: 17px; height: 14px; fill: var(--brand-red); flex: none; }
</style>
</head>
<body>
<main class="canvas">
  <section class="card card--front">
    <div class="front__wordmark">Kelvaro</div>
    <div class="front__url">www.kelvaro.se</div>
  </section>

  <section class="card card--back">
    <div class="back__accent"></div>
    <div class="back__divider"></div>
    <div class="back__wordmark">Kelvaro</div>
    <div class="back__name">Tobias Vrenholt</div>
    <div class="back__title">CEO</div>
    <ul class="contact">
      <li class="contact__item">
        <svg class="contact__icon" viewBox="0 0 17 14" aria-hidden="true">
          <path d="M1 5 C1 1 16 1 16 5 L16 6 L12 6 L12 4 C10 3 7 3 5 4 L5 6 L1 6 Z"/>
          <path d="M5 6 L12 6 L15 13 L2 13 Z"/>
          <circle cx="8.5" cy="9.5" r="2" fill="#fff"/>
        </svg>
        <span>+46 712 418257</span>
      </li>
      <li class="contact__item">
        <svg class="contact__icon" viewBox="0 0 17 14" aria-hidden="true">
          <rect x="0" y="1" width="17" height="12"/>
          <path d="M1.5 2.5 L8.5 8 L15.5 2.5 M1.5 11.5 L6.5 7 M15.5 11.5 L10.5 7" stroke="#fff" stroke-width="1.3" fill="none"/>
        </svg>
        <span>tobias@kelvaro.se</span>
      </li>
    </ul>
  </section>
</main>
</body>
</html>
```